Current Employment Opportunities Email Template

We would like to redesign our internal job listing email template we send out each month. The email service we use is MailChimp and would like the template to be easy to edit when updating job postings. I attached an example below.

Font styles to use
Sans Serif

Colors

Designer to choose colors to be used in the design.

```html
<!DOCTYPE html>
<html lang="en">
<head>
<meta charset="utf-8">
<title>Today's Talent Opportunities – Ridgeway Services Inc.</title>
<link href="https://fonts.googleapis.com/css2?family=Nunito+Sans:wght@300;400;600;700;800&display=swap" rel="stylesheet">
<style>
  :root {
    --page-bg: #ebebeb;
    --card-bg: #ffffff;
    --brand-green: #0aa24b;
    --mint: #eefaf3;
    --ink-dark: #4f5250;
    --ink-body: #7a7a7a;
    --ink-muted: #8a8a8a;
    --rule: #dcdcdc;
    --alert-red: #e0262b;
  }
  * { box-sizing: border-box; margin: 0; padding: 0; }
  html, body {
    width: 701px; height: 1200px; overflow: hidden;
    background: var(--page-bg);
    font-family: "Nunito Sans", Arial, sans-serif;
  }
  .preheader {
    position: absolute; top: 40px; left: 0; width: 701px;
    text-align: center; font-size: 10px; font-weight: 700; color: var(--ink-muted); line-height: 13px;
  }
  .preheader a { color: var(--alert-red); text-decoration: underline; }

  .email-card {
    position: absolute; left: 134px; top: 91px; width: 432px; height: 946px;
    background: var(--card-bg); border-radius: 7px; overflow: hidden;
  }
  .brand-name {
    position: absolute; top: 34px; left: 0; width: 100%; text-align: center;
    font-size: 22px; font-weight: 800; color: #1c1c1c; letter-spacing: 1px; text-transform: uppercase;
  }
  .header-rule { position: absolute; left: 18px; top: 81px; width: 396px; height: 3px; background: #e2e2e2; }
  .intro-title {
    position: absolute; top: 93px; width: 100%; text-align: center;
    font-size: 23px; font-weight: 800; color: var(--brand-green); line-height: 30px;
  }
  .intro-subtitle {
    position: absolute; top: 124px; width: 100%; text-align: center;
    font-size: 11px; font-weight: 700; color: var(--ink-dark);
  }
  .intro-copy {
    position: absolute; left: 18px; top: 145px; width: 400px;
    font-size: 12px; line-height: 19.5px; color: var(--ink-body);
  }

  .openings { position: absolute; left: 0; top: 294px; width: 432px; height: 532px; background: var(--mint); }
  .openings-band { position: absolute; left: 0; top: 0; }
  .openings-label {
    position: absolute; left: 0; top: 0;
  }
  .openings-label-text {
    position: absolute; left: 94px; top: 10px; width: 246px; height: 33px; line-height: 33px;
    text-align: center; font-size: 13px; font-weight: 800; color: var(--brand-green); letter-spacing: .2px;
  }
  .openings-footer-rule { position: absolute; left: 0; bottom: 0; width: 432px; height: 5px; background: var(--brand-green); }

  .job-row { position: absolute; left: 0; width: 432px; height: 100px; }
  .job-city {
    position: absolute; left: 0; top: 32px; width: 132px; padding-left: 14px;
    font-size: 27px; font-weight: 300; color: var(--brand-green); line-height: 30px; letter-spacing: .5px;
  }
  .job-divider { position: absolute; left: 132px; top: 0; width: 2px; height: 100px; background: #d6d6d6; }
  .job-title { position: absolute; left: 153px; top: 3px; font-size: 13px; font-weight: 800; color: var(--ink-dark); line-height: 16px; }
  .job-location { position: absolute; left: 153px; top: 22px; font-size: 12px; color: var(--brand-green); line-height: 16px; }
  .job-summary { position: absolute; left: 153px; top: 43px; font-size: 9.6px; font-weight: 700; color: var(--ink-dark); line-height: 13px; }
  .job-button {
    position: absolute; left: 153px; top: 65px; width: 205px; height: 29px; border-radius: 15px;
    background: var(--brand-green); color: #fff; font-size: 10px; font-weight: 700;
    text-align: center; line-height: 29px; text-decoration: none;
  }
  .row-separator { position: absolute; left: 18px; width: 396px; height: 1px; background: #cfd8d2; }

  .footer-contact {
    position: absolute; left: 141px; top: 862px; height: 24px; display: flex; align-items: center; gap: 7px;
    font-size: 12px; color: var(--ink-dark);
  }
  .footer-rule { position: absolute; left: 18px; top: 895px; width: 396px; height: 1px; background: #e3e3e3; }
  .footer-copyright { position: absolute; left: 18px; top: 906px; font-size: 10.5px; color: var(--ink-dark); }
  .footer-social { position: absolute; left: 311px; top: 902px; display: flex; gap: 4px; }
  .social-dot { width: 22px; height: 22px; border: 1.5px solid #8d8d8d; border-radius: 50%; }
</style>
</head>
<body>
  <p class="preheader">Is this email not displaying correctly?<br><a href="#">View it in your browser.</a></p>

  <main class="email-card">
    <div class="brand-name">Ridgeway Services Inc.</div>
    <div class="header-rule"></div>

    <h1 class="intro-title">Today's Talent Oppurtunities</h1>
    <p class="intro-subtitle">Want to be a part of the most efficient and elite team in the industry?</p>
    <p class="intro-copy">We've got a list of opportunities here at Ridgeway that we'd love for you to strive for! These openings allow you to fully tuilize your strengths, walk alongside us as we grow exponentially farther than we could ever dream. and leverage your successes to climb your way up the ladder of professional growth and leadership withing our organization!</p>

    <section class="openings">
      <svg class="openings-band" width="432" height="80" viewBox="0 0 432 80">
        <polygon points="0,-1 432,-1 432,23 0,11" fill="var(--brand-green)"/>
        <path d="M100,10 H334 a6,6 0 0 1 6,6 V37 a6,6 0 0 1 -6,6 H230 L216,57 L202,43 H100 a6,6 0 0 1 -6,-6 V16 a6,6 0 0 1 6,-6 Z" fill="#fff" stroke="var(--brand-green)" stroke-width="2"/>
        <circle cx="201" cy="1" r="15" fill="var(--brand-green)"/>
        <g transform="translate(201 1)">
          <path d="M-7,-2 L3,-7 L3,7 L-7,2 Z" fill="#f2c230"/>
          <rect x="-9" y="-2.5" width="3" height="5" fill="#fff"/>
          <path d="M-6,2 L-4,7 L-2,7 L-3,2 Z" fill="#fff"/>
          <path d="M5,-3 Q8,0 5,3" stroke="#fff" stroke-width="1.5" fill="none"/>
        </g>
      </svg>
      <div class="openings-label-text">CURRENT OPPORTUNITIES</div>

      <article class="job-row" style="top:85px">
        <div class="job-city">DALLAS</div>
        <div class="job-divider"></div>
        <h2 class="job-title">REGIONAL SALES MANGER</h2>
        <p class="job-location">DALLAS,TX</p>
        <p class="job-summary">Restoration Technician in the Dallas/Ft. Worth Area</p>
        <a class="job-button" href="#">Learn More About This Opportunity</a>
      </article>
      <div class="row-separator" style="top:202px"></div>

      <article class="job-row" style="top:236px">
        <div class="job-city">AUSTIN</div>
        <div class="job-divider"></div>
        <h2 class="job-title">JANITORIAL SALES/ACCOUNT MANAGER</h2>
        <p class="job-location">AUSTIN,TX</p>
        <p class="job-summary">Rewarding, fufilling and goal oriented position..</p>
        <a class="job-button" href="#">Learn More About This Opportunity</a>
      </article>
      <div class="row-separator" style="top:354px"></div>

      <article class="job-row" style="top:382px">
        <div class="job-city">DENVER</div>
        <div class="job-divider"></div>
        <h2 class="job-title">JANITORIAL SALES/ACCOUNT MANGER</h2>
        <p class="job-location">DENVER,CO</p>
        <p class="job-summary">Rewarding, fufilling and goal oriented position..</p>
        <a class="job-button" href="#">Learn More About This Opportunity</a>
      </article>

      <div class="openings-footer-rule"></div>
    </section>

    <div class="footer-contact">
      <svg width="22" height="22" viewBox="0 0 22 22">
        <circle cx="11" cy="11" r="10" fill="#fff" stroke="#e0e0e0"/>
        <rect x="6" y="7.5" width="10" height="7" rx="1" fill="var(--brand-green)"/>
        <path d="M6.5,8 L11,11.5 L15.5,8" stroke="#fff" stroke-width="1.2" fill="none"/>
      </svg>
      <span>hello@ridgewayteam.com</span>
    </div>
    <div class="footer-rule"></div>
    <p class="footer-copyright">Copyright © 2018 Your Website - All Rights Reserved.</p>
    <div class="footer-social">
      <span class="social-dot"></span><span class="social-dot"></span><span class="social-dot"></span><span class="social-dot"></span>
    </div>
  </main>
</body>
</html>
```